Business Card Design

I need a business card for my baking business. Name of the company is Whisked by Tessa. I specialize in cookies and pies.
I don't make cupcakes or cakes. I would like a design with colors of brown, light pink and dark pink and maybe have the half eaten cookie be the dot of the "I" in my name. (Half eaten chocolate chip and the chips being hot pink light pink and brown chips).. I would like the card fun and modern design.
On the back of the card tag line- sweeten up your hours

Industry/Entity Type

Business

Contact Information for Business Card

Tessa Mernholt
Cell 5093617284
Email-Tesmern47@quillpost.net

```html
<!DOCTYPE html>
<html lang="en">
<head>
<meta charset="utf-8">
<title>Whisked by Tessa – Business Card</title>
<link href="https://fonts.googleapis.com/css2?family=Comfortaa:wght@700&family=Great+Vibes&family=Lato:wght@400&display=swap" rel="stylesheet">
<style>
  :root {
    --backdrop: #1c1a1d;
    --cocoa-light: #5a3a3a;
    --cocoa: #452b2b;
    --cocoa-dark: #2f1d1e;
    --pink-hot: #d96aa3;
    --pink-soft: #f2c2da;
    --cream: #ffffff;
  }
  * { box-sizing: border-box; margin: 0; padding: 0; }
  html, body {
    width: 1200px; height: 1200px; overflow: hidden;
    background: var(--backdrop);
  }
  .sheet {
    width: 1200px; height: 1200px;
    display: flex; flex-direction: column; align-items: center; justify-content: center;
    gap: 70px;
  }
  .card {
    position: relative;
    width: 900px; height: 514px;
    overflow: hidden;
    background: radial-gradient(circle at 45% 45%, var(--cocoa-light) 0%, var(--cocoa) 45%, var(--cocoa-dark) 100%);
  }
  .brand {
    display: flex; align-items: center; gap: 18px;
    white-space: nowrap;
  }
  .brand-name {
    font-family: "Comfortaa", sans-serif; font-weight: 700;
    font-size: 64px; color: var(--pink-hot); letter-spacing: 1px;
  }
  .brand-dot {
    width: 34px; height: 34px; border-radius: 50%;
    background: var(--pink-soft); flex: none;
  }

  /* Front */
  .card-front .brand {
    position: absolute; left: 0; right: 0; top: 170px;
    justify-content: center;
  }
  .tagline {
    position: absolute; left: 0; right: 0; top: 320px;
    text-align: center;
    font-family: "Great Vibes", cursive; font-size: 54px;
    color: var(--pink-soft);
  }

  /* Back */
  .card-back .contact {
    position: absolute; left: 60px; top: 190px;
    color: var(--cream);
  }
  .person {
    font-family: "Comfortaa", sans-serif; font-weight: 700;
    font-size: 34px; margin-bottom: 26px;
  }
  .contact-line {
    display: flex; align-items: center; gap: 12px;
    font-family: "Lato", sans-serif; font-size: 21px;
    margin-bottom: 10px;
  }
  .contact-line svg { width: 22px; height: 22px; flex: none; }
  .logo-disc {
    position: absolute; left: 470px; top: -130px;
    width: 780px; height: 780px; border-radius: 50%;
    background: var(--cream);
    border: 14px solid var(--pink-hot);
  }
  .card-back .brand {
    position: absolute; left: 520px; top: 232px;
    gap: 10px;
  }
  .card-back .brand-name { font-size: 34px; letter-spacing: 0; }
  .card-back .brand-dot { width: 20px; height: 20px; background: var(--pink-hot); }
</style>
</head>
<body>
<main class="sheet">
  <section class="card card-front" aria-label="Card front">
    <div class="brand">
      <span class="brand-name">Whisked by Tessa</span>
      <span class="brand-dot"></span>
    </div>
    <p class="tagline">sweeten up your hours</p>
  </section>

  <section class="card card-back" aria-label="Card back">
    <div class="contact">
      <p class="person">Tessa Mernholt</p>
      <p class="contact-line">
        <svg viewBox="0 0 24 24" aria-hidden="true"><rect x="6" y="2" width="12" height="20" rx="2" fill="none" stroke="var(--pink-hot)" stroke-width="2"/><circle cx="12" cy="18" r="1.3" fill="var(--pink-hot)"/></svg>
        5093617284
      </p>
      <p class="contact-line">
        <svg viewBox="0 0 24 24" aria-hidden="true"><rect x="2" y="5" width="20" height="14" rx="1" fill="var(--pink-hot)"/><path d="M2 6 L12 13 L22 6" fill="none" stroke="var(--cocoa)" stroke-width="1.6"/></svg>
        Tesmern47@quillpost.net
      </p>
    </div>
    <div class="logo-disc"></div>
    <div class="brand">
      <span class="brand-name">Whisked by Tessa</span>
      <span class="brand-dot"></span>
    </div>
  </section>
</main>
</body>
</html>
```